The Dorval Lodge 5 Bedroom Cayman Islands Guest House offering weekly rentals

I am in need of a website for my 5 bedroom guest house in the Cayman Islands.
I have operated this guest house for almost three years. As the sites I am currently located on have raised their charges over the past year; I have decided to host my own site.
The site should reflect island retreat type style. With Tropical, ocean colors
Here are the core requirements I can think of.
• A comprehensive vacation rental web site
• Multiple languages if possible
• Pictures & video – of property, what’s close & the island
• Property description
• Reservation/Booking calendar.
• Information on where to go
• Social media links, such as a PalBoard & Snapgrid
• Shared moments - Event, celebration and guest photos
• Reviews page
• Rates
• Email interaction/Messaging
• Credit card processing… (Be able to securely hold the credit card information to manually process using a credit card machine (Within 24 hours)
I have already started a site on NetHarbor but got lost so once agreed I would hand over the codes as they would also be hosting the site.

Info on the house:

This spacious vacation home is a 5 minute walk away from Coral Point Public Beach and has a supermarket across the street. A small shopping plaza with a bank, pharmacy and 24 hour Hoagies is a one minute walk away. No car? No problem! The public bus stops right in front of the house, runs along Long Shell Beach and on to George Town. Take a 5 minute bus ride to Palmora Quay; an outdoor mall with restaurants, shops, Filmdome and home to the islands only observation tower.

The home boasts a fully loaded kitchen with granite counter tops, six burner gas stove, large capacity refrigerator and two dishwashers perfect for feeding a large family or group.
State of the art media room with a 73 inch high definition television, GX4, complete surround sound and plush recliners providing hours of entertainment.
Downstairs, the master suite has a comfortable memory foam king bed and an en-suite bathroom with a granite double vanity and whirlpool tub. Perfect for relaxing after a long day at the beach. Downstairs also has a cozy Queen bedroom and a serene King bedroom that shares a full bathroom. There’s an additional half-bath for added convenience.
The upstairs is a spacious double Queen bedroom and a double Full bedroom that shares a bathroom. In total the house sleeps up to 14 people very comfortably.
The screened in back porch can be accessed from the media room, downstairs Master bedroom and Queen bedroom. It’s the ideal escape to enjoy the fresh Cayman breeze without the insects.
To spare you the hassle of laundry; we’ve even provided two washers and two dryers! Leaving you more time for the beach.
For the vacation Mom, no need to worry, we have a full size crib, Tot-A-Lot Play pen, 2 full size high chairs and a car seat!

Target Market(s)

Families or groups seeking to vacation in the Caribbean or the tropics.

Industry/Entity Type

Hotel

Contact Information for Business Card

Business card front
The Dorval Lodge
Guest House
Your Cayman home away from home!
1187 Harbor View Rd, Grand Cayman, Cayman Islands
Tel: (345) 555-0147
Email: thedorvallodge@mailnest.example

Business card back
Pictures of house
5 bedroom home walking distance to the beach!
Air-conditioned, Wi-Fi, cable TV, sleeps up to 14
Book online www.thedorvallodge.example
Like us on PalBoard

Number of Pages Required

5+ page

Font styles to use
Script

Requirements
Must have
• Multiple languages if possible (English, Spanish, French)
• • Pictures & video – of property, what’s close & the island
• • Property description
• • Reservation/Booking calendar.
• • Information on where to go
• • Social media links, such as a PalBoard & Snapgrid
• • Shared moments - Event, celebration and guest photos
• • Reviews page
• • Rates
• • Email interaction/Messaging
• • Credit card processing… (Be able to securely hold the credit card information to manually process using a credit card machine (Within 24 hours)
Nice to have
• Slide show of the house on the home page
Should not have
• Too many dark colors

```html
<!DOCTYPE html>
<html lang="en">
<head>
<meta charset="utf-8">
<title>Dorval Lodge – Guest House</title>
<link href="https://fonts.googleapis.com/css2?family=Roboto:wght@400;500;700&family=Open+Sans:wght@400;600&display=swap" rel="stylesheet">
<style>
:root{
  --blue:#1e8be6;
  --blue-dark:#1572c2;
  --ink:#1f1f1f;
  --nav:#232323;
  --text:#555;
  --muted:#8a8a8a;
  --line:#d9d9d9;
  --panel:#dcdcdc;
  --footer:#303233;
  --footer-deep:#232425;
  --white:#fff;
}
*{box-sizing:border-box;margin:0;padding:0}
html,body{width:1200px;height:3435px;overflow:hidden}
body{position:relative;background:var(--white);font-family:"Open Sans",Arial,sans-serif;color:var(--text)}
.abs{position:absolute}
h1,h2,h3,h4,.nav a,.btn{font-family:"Roboto",Arial,sans-serif}

/* header */
.site-header{top:0;left:0;width:1200px;height:105px}
.brand{left:92px;top:30px;display:flex;align-items:center;gap:12px;color:var(--blue);font:700 24px "Roboto",sans-serif;letter-spacing:1px}
.brand-dot{width:40px;height:40px;border-radius:50%;background:var(--blue)}
.social{left:650px;top:48px;width:240px;display:flex;justify-content:flex-end;gap:14px;font:500 13px "Roboto",sans-serif;color:var(--blue);white-space:nowrap}
.search-box{left:911px;top:34px;width:64px;height:46px;border:1px solid var(--line);display:flex;align-items:center;justify-content:center}
.lang{left:1008px;top:34px;width:100px;height:46px;border:1px solid var(--line);display:flex;align-items:center;justify-content:center;gap:14px;font:500 13px "Roboto",sans-serif;color:var(--ink)}

.nav{top:105px;left:0;width:1200px;height:60px;background:var(--nav)}
.nav a{position:absolute;top:21px;color:var(--white);text-decoration:none;font-size:14px;font-weight:500}

/* hero */
.hero{top:165px;left:0;width:1200px;height:442px;background:linear-gradient(120deg,#1a7fd0 0%,#2c9be2 30%,#5bb8ec 48%,#e8e2d4 62%,#d9b76c 78%,#f2efe8 100%)}
.hero h1{position:absolute;left:160px;top:112px;color:var(--ink);font-size:32px;font-weight:700}
.hero p{position:absolute;left:164px;top:166px;width:440px;color:var(--ink);font:400 19px/28px "Roboto",sans-serif}
.btn{position:absolute;display:flex;align-items:center;justify-content:center;font-size:13px;font-weight:500;color:var(--white)}
.btn-pill{border-radius:20px;height:38px;width:174px;top:265px}

/* availability */
.availability{top:607px;left:0;width:1200px;height:117px;background:var(--blue)}
.availability .dark{position:absolute;left:0;top:0}
.availability h3{position:absolute;left:122px;top:32px;color:var(--white);font-size:20px;line-height:26px;font-weight:500}
.field-label{position:absolute;top:24px;color:var(--white);font-size:14px}
.date-field{position:absolute;top:57px;height:36px;width:151px;background:var(--white);border:1px solid #bcd}
.date-field span{position:absolute;right:3px;top:3px;width:28px;height:28px;background:#eee;display:flex;align-items:center;justify-content:center}
.select{position:absolute;top:57px;height:36px;width:87px;background:var(--white)}
.select b{position:absolute;left:12px;top:8px;font:400 14px "Roboto",sans-serif;color:var(--ink)}
.select span{position:absolute;right:0;top:0;width:40px;height:36px;border-left:1px solid var(--line);display:flex;align-items:center;justify-content:center}
.check-btn{left:992px;top:57px;width:98px;height:37px;background:var(--white);color:var(--ink);font-size:13px;font-weight:700}

/* section titles */
.section-title{position:absolute;left:0;width:1200px;text-align:center;color:var(--ink);font-size:23px;font-weight:700}
.lead{position:absolute;left:300px;width:600px;text-align:center;font-size:13px;line-height:22px;color:var(--muted)}

/* rooms */
.room{position:absolute;top:946px;width:238px}
.room-photo{width:238px;height:167px}
.room h4{position:absolute;top:232px;left:0;font-size:14px;font-weight:500;color:var(--ink)}
.room .price{position:absolute;top:258px;left:0;font:500 14px "Roboto",sans-serif;color:var(--ink)}
.room .book{position:absolute;top:233px;left:152px;width:84px;height:37px;border:2px solid var(--blue);display:flex;align-items:center;justify-content:center;font:500 10px "Roboto",sans-serif;color:var(--ink)}

/* facilities */
.facilities-band{top:1374px;left:0;width:1200px;height:440px;background:linear-gradient(90deg,#9b9a9c,#d9d8db 30%,#eceaec 55%,#b3b1b3 80%,#8c8a8d)}
.facilities-card{left:108px;top:62px;width:950px;height:316px;background:var(--white)}
.video{left:27px;top:27px;width:458px;height:259px;background:linear-gradient(135deg,#3a3a3a,#6b6b6b 45%,#2f2f2f)}
.video-bar{position:absolute;left:0;bottom:0;width:100%;height:22px;background:#151515}
.play{position:absolute;left:194px;top:103px;width:62px;height:42px;background:var(--white);border-radius:8px;display:flex;align-items:center;justify-content:center}
.facilities-card h3{position:absolute;left:524px;top:34px;font-size:25px;font-weight:700;color:var(--ink)}
.facilities-card p{position:absolute;left:524px;width:400px;font-size:11px;line-height:16px;color:var(--muted)}
.fac-links{position:absolute;left:524px;top:199px;display:flex;gap:36px;font-size:10px;color:var(--blue)}
.dark-btn{left:540px;top:243px;width:108px;height:34px;background:var(--ink);font-size:12px}

/* reservation */
.reservation{top:1814px;left:0;width:1200px;height:467px;background:var(--panel)}
.reservation .section-title{top:24px}
.input{position:absolute;height:32px;background:var(--white);font:500 11px "Roboto",sans-serif;color:#666;padding-left:16px;display:flex;align-items:center;text-transform:uppercase}
.cards{position:absolute;right:12px;top:8px;display:flex;gap:8px;font:700 9px "Roboto",sans-serif;color:var(--blue-dark)}
.pay-btn{left:536px;top:407px;width:133px;height:39px;background:var(--blue);font-size:13px}

/* blog */
.post{position:absolute;top:2372px;width:257px;height:348px;border-bottom:1px solid var(--line)}
.post-photo{width:257px;height:202px}
.post h4{position:absolute;top:224px;left:20px;font-size:13px;font-weight:500;color:var(--ink)}
.post .meta{position:absolute;top:243px;left:20px;font-size:9px;color:var(--muted)}
.post .meta i{font-style:normal;color:var(--blue)}
.post p{position:absolute;top:264px;left:20px;width:215px;font-size:10px;line-height:15px;color:#999}
.post .more{position:absolute;top:324px;left:20px;font:500 10px "Roboto",sans-serif;color:var(--ink)}

/* reviews */
.review{position:absolute;top:2860px;width:450px}
.stars{position:absolute;top:10px;left:0}
.review h4{position:absolute;left:126px;top:0;font:500 20px "Roboto",sans-serif;color:var(--ink)}
.avatar{position:absolute;left:0;top:71px;width:100px;height:100px;border-radius:50%}
.review p{position:absolute;left:135px;top:90px;width:300px;font-size:9px;line-height:14px;color:var(--muted)}
.review .name{position:absolute;left:0;top:198px;font:400 16px "Roboto",sans-serif;color:var(--ink)}

/* footer */
.footer{top:3105px;left:0;width:1200px;height:280px;background:var(--footer)}
.footer h4{position:absolute;top:44px;font:500 12px "Roboto",sans-serif;color:#cfcfcf;letter-spacing:.5px}
.footer .col-text{position:absolute;top:78px;width:175px;font-size:9.5px;line-height:14px;color:#9a9a9a}
.contact-row{position:absolute;display:flex;gap:10px;font-size:9px;line-height:14px;color:#9a9a9a;max-width:190px}
.post-row{position:absolute;left:609px;display:flex;gap:10px}
.post-thumb{width:38px;height:38px;background:linear-gradient(135deg,#c98a5b,#5a8fb8)}
.post-row b{display:block;font:500 10px "Roboto",sans-serif;color:var(--blue)}
.post-row span{font-size:9px;color:#888}
.email-input{position:absolute;left:808px;top:198px;width:140px;height:30px;background:#3c3e40;font-size:10px;color:#888;padding:8px 12px}
.email-send{position:absolute;left:952px;top:198px;width:30px;height:30px;background:#37b3c7;display:flex;align-items:center;justify-content:center}
.footer-social{position:absolute;left:410px;top:186px;display:flex;gap:10px;font-size:8px;color:#aaa}
.bottom-bar{top:3385px;left:0;width:1200px;height:50px;background:var(--footer-deep)}
.bottom-bar p{position:absolute;left:0;width:1200px;top:18px;text-align:center;font-size:9px;color:#ccc}
.to-top{position:absolute;left:960px;top:11px;width:28px;height:28px;border:1px solid #37b3c7;border-radius:50%;display:flex;align-items:center;justify-content:center}
</style>
</head>
<body>

<header class="abs site-header">
  <div class="abs brand"><span class="brand-dot"></span>DORVAL LODGE</div>
  <div class="abs social"><span>Chirp</span><span>PlusOne</span><span>WorkLink</span><span>PalBoard</span></div>
  <div class="abs search-box">
    <svg width="18" height="18" viewBox="0 0 18 18"><circle cx="7.5" cy="7.5" r="5.5" fill="none" stroke="#222" stroke-width="2"/><line x1="11.5" y1="11.5" x2="16" y2="16" stroke="#222" stroke-width="2.4"/></svg>
  </div>
  <div class="abs lang"><span>ENG</span><span>ESP</span></div>
</header>

<nav class="abs nav">
  <a style="left:105px">HOME</a><a style="left:199px">FEATURES</a><a style="left:325px">SERVICES</a><a style="left:447px">WORKS</a><a style="left:550px">GALLERY</a><a style="left:680px">NEWS</a><a style="left:792px">CONTACT</a>
</nav>

<section class="abs hero" role="img" aria-label="Sunny island terrace with umbrella and chairs overlooking a deep blue sea">
  <h1>WELCOME TO DORVAL LODGE!</h1>
  <p>We Love To Make You Feel More Comfortable On Your Home.</p>
  <a class="btn btn-pill" style="left:160px;background:var(--blue)">BOOK NOW</a>
  <a class="btn btn-pill" style="left:366px;background:var(--ink)">GET STARTED</a>
</section>

<section class="abs availability">
  <svg class="dark" width="380" height="117"><polygon points="0,0 300,0 366,117 0,117" fill="#262626"/></svg>
  <h3>CHECK<br>AVAILABILITY</h3>
  <span class="field-label" style="left:412px">Arrival Date</span>
  <span class="field-label" style="left:573px">Departure Date</span>
  <span class="field-label" style="left:767px">Adults</span>
  <span class="field-label" style="left:875px">Children</span>
  <div class="date-field" style="left:385px"><span><svg width="14" height="14" viewBox="0 0 14 14"><rect x="1" y="2" width="12" height="11" fill="none" stroke="#777" stroke-width="1.4"/><line x1="1" y1="5.5" x2="13" y2="5.5" stroke="#777" stroke-width="1.4"/></svg></span></div>
  <div class="date-field" style="left:561px"><span><svg width="14" height="14" viewBox="0 0 14 14"><rect x="1" y="2" width="12" height="11" fill="none" stroke="#777" stroke-width="1.4"/><line x1="1" y1="5.5" x2="13" y2="5.5" stroke="#777" stroke-width="1.4"/></svg></span></div>
  <div class="select" style="left:737px"><b>1</b><span><svg width="12" height="8"><polyline points="1,1 6,6 11,1" fill="none" stroke="#333" stroke-width="2"/></svg></span></div>
  <div class="select" style="left:854px"><b>1</b><span><svg width="12" height="8"><polyline points="1,1 6,6 11,1" fill="none" stroke="#333" stroke-width="2"/></svg></span></div>
  <a class="btn check-btn">CHECK</a>
</section>

<h2 class="section-title" style="top:790px">NEED AWSOME ROOMS</h2>
<p class="lead" style="top:850px">Semper ac dolor vitae accumsan. Cras interdum hendrerit lacinia. Phasellus accumsan urna vitae molestie interdum. Nam sed placerat libero, non eleifend dolor.</p>

<div class="room" style="left:82px">
  <div class="room-photo" role="img" aria-label="Bright bedroom with a yellow headboard and framed pictures" style="background:linear-gradient(180deg,#f4f1ec 0%,#ece7de 55%,#e5c42c 70%,#f7f5f0 100%)"></div>
  <h4>5 BED ROOMS</h4><span class="price">$200/ night</span><a class="book">BOOK NOW</a>
</div>
<div class="room" style="left:346px">
  <div class="room-photo" role="img" aria-label="Bedroom with deep red walls and white bedding" style="background:linear-gradient(90deg,#3e1f24 0%,#6e2d37 35%,#efe9e6 60%,#7a3340 100%)"></div>
  <h4>5 BED ROOMS</h4><span class="price">$200/ night</span><a class="book">BOOK NOW</a>
</div>
<div class="room" style="left:611px">
  <div class="room-photo" role="img" aria-label="Light living room with a grey sofa and round wooden table" style="background:linear-gradient(180deg,#f2f1ef 0%,#e3e1de 50%,#b7b2aa 75%,#9b6f48 100%)"></div>
  <h4>5 BED ROOMS</h4><span class="price">$200/ night</span><a class="book">BOOK NOW</a>
</div>
<div class="room" style="left:877px">
  <div class="room-photo" role="img" aria-label="Warm lounge with orange chairs and a patterned rug" style="background:linear-gradient(135deg,#6b4a2e 0%,#d89b2b 40%,#e8e1d3 65%,#b5542e 100%)"></div>
  <h4>5 BED ROOMS</h4><span class="price">$200/ night</span><a class="book">BOOK NOW</a>
</div>

<h2 class="section-title" style="top:1310px">GUEST ROOM FACILITIES</h2>

<section class="abs facilities-band" role="img" aria-label="Hotel lobby with a reception desk in soft grey tones">
  <div class="abs facilities-card">
    <div class="abs video" role="img" aria-label="Video of a modern guest bedroom">
      <div class="play"><svg width="20" height="22"><polygon points="2,1 19,11 2,21" fill="#222"/></svg></div>
      <div class="video-bar"><svg width="458" height="22"><rect x="10" y="7" width="3" height="8" fill="#ccc"/><rect x="15" y="7" width="3" height="8" fill="#ccc"/><polygon points="440,8 444,8 448,5 448,17 444,14 440,14" fill="#ccc"/></svg></div>
    </div>
    <h3>GUEST ROOM FACILITIES</h3>
    <p style="top:80px">Semper ac dolor vitae accumsan. Cras interdum hendrerit lacinia. Phasellus accumsan urna vitae molestie interdum. Nam sed placerat libero, non eleifend dolor.</p>
    <p style="top:136px">Cras ut justo et augue suscipit euismod vel eget lectus. Proin vehicula nunc arcu, pulvinar accumsan nulla porta vel. Vivamus malesuada vitae sem ac pellentesque.</p>
    <div class="fac-links"><span>SERVICE HOURS: READ MORE</span><span>SERVICE CHARGE: $15</span></div>
    <a class="btn dark-btn">BOOK NOW</a>
  </div>
</section>

<section class="abs reservation">
  <h2 class="section-title">MAKE A RESERVATION</h2>
  <div class="input" style="left:131px;top:105px;width:377px">First Name</div>
  <div class="input" style="left:611px;top:105px;width:378px">Email ID</div>
  <div class="input" style="left:131px;top:178px;width:377px">Phone Number</div>
  <div class="input" style="left:611px;top:178px;width:378px">Address</div>
  <div class="input" style="left:131px;top:252px;width:377px">Name of Card</div>
  <div class="input" style="left:611px;top:252px;width:378px">Card Type<span class="cards"><span>PayWell</span><span>CardOne</span><span>MeshCard</span></span></div>
  <div class="input" style="left:131px;top:316px;width:377px">Credit Card No</div>
  <div class="input" style="left:611px;top:316px;width:143px">Expiration Date <svg style="margin-left:8px" width="9" height="6"><polygon points="0,0 9,0 4.5,6" fill="#444"/></svg></div>
  <div class="input" style="left:757px;top:316px;width:140px"><svg style="margin-left:110px" width="9" height="6"><polygon points="0,0 9,0 4.5,6" fill="#444"/></svg></div>
  <div class="input" style="left:900px;top:316px;width:89px">CCV</div>
  <a class="btn pay-btn">PAY NOW</a>
</section>

<h2 class="section-title" style="top:2320px">LATEST BLOG POSTS</h2>

<article class="post" style="left:94px">
  <div class="post-photo" role="img" aria-label="Diver leaping over a pool against a pale sky" style="background:linear-gradient(180deg,#dfe6ee 0%,#eef1f4 60%,#c8b6a6 85%,#9f8f82 100%)"></div>
  <h4>EXCEPTEUR SINT OCCAECAT</h4><span class="meta">12 December, 2015 &nbsp;|&nbsp; by <i>Ana Reyes</i></span>
  <p>Lorem ipsum dolor sit amet, consectetur adipiscing elit, sed do eiusmod tempor incididunt ut labore et dolore magna aliqua.</p><span class="more">READ MORE...</span>
</article>
<article class="post" style="left:355px">
  <div class="post-photo" role="img" aria-label="Boat on turquoise lagoon water under a blue sky" style="background:linear-gradient(180deg,#3b8fd6 0%,#8cc7ec 45%,#2fc0c3 65%,#1a9ea8 100%)"></div>
  <h4>EXCEPTEUR SINT OCCAECAT</h4><span class="meta">12 December, 2015 &nbsp;|&nbsp; by <i>Ana Reyes</i></span>
  <p>Lorem ipsum dolor sit amet, consectetur adipiscing elit, sed do eiusmod tempor incididunt ut labore et dolore magna aliqua.</p><span class="more">READ MORE...</span>
</article>
<article class="post" style="left:616px">
  <div class="post-photo" role="img" aria-label="Round white lounge beds beside a pool by the sea" style="background:linear-gradient(180deg,#9fc6e4 0%,#5d8fb5 40%,#e9e3d8 60%,#6a5a4c 100%)"></div>
  <h4>EXCEPTEUR SINT OCCAECAT</h4><span class="meta">12 December, 2015 &nbsp;|&nbsp; by <i>Ana Reyes</i></span>
  <p>Lorem ipsum dolor sit amet, consectetur adipiscing elit, sed do eiusmod tempor incididunt ut labore et dolore magna aliqua.</p><span class="more">READ MORE...</span>
</article>
<article class="post" style="left:877px">
  <div class="post-photo" role="img" aria-label="Sun deck with striped loungers overlooking the harbour" style="background:linear-gradient(180deg,#2f86d1 0%,#6fb1e3 40%,#c7b08a 60%,#d7632b 85%,#8a4f2a 100%)"></div>
  <h4>EXCEPTEUR SINT OCCAECAT</h4><span class="meta">12 December, 2015 &nbsp;|&nbsp; by <i>Ana Reyes</i></span>
  <p>Lorem ipsum dolor sit amet, consectetur adipiscing elit, sed do eiusmod tempor incididunt ut labore et dolore magna aliqua.</p><span class="more">READ MORE...</span>
</article>

<h2 class="section-title" style="top:2788px;font-size:17px">THIS IS WHAT OUR GUEST THINK</h2>

<div class="review" style="left:153px">
  <svg class="stars" width="84" height="18" viewBox="0 0 84 18"><g fill="#1e8be6"><polygon points="9,0 11.6,6 18,6.6 13.2,10.8 14.6,17 9,13.7 3.4,17 4.8,10.8 0,6.6 6.4,6"/><polygon transform="translate(21 0)" points="9,0 11.6,6 18,6.6 13.2,10.8 14.6,17 9,13.7 3.4,17 4.8,10.8 0,6.6 6.4,6"/><polygon transform="translate(42 0)" points="9,0 11.6,6 18,6.6 13.2,10.8 14.6,17 9,13.7 3.4,17 4.8,10.8 0,6.6 6.4,6"/></g><polygon transform="translate(63 0)" points="9,0 11.6,6 18,6.6 13.2,10.8 14.6,17 9,13.7 3.4,17 4.8,10.8 0,6.6 6.4,6" fill="#b9cfe6"/></svg>
  <h4>“Worth To Come Again”</h4>
  <div class="avatar" role="img" aria-label="Portrait of a smiling couple" style="background:linear-gradient(135deg,#c88e6a,#8b6a55)"></div>
  <p>Really good location: in walking distance to almost every spot on the bay. Nice house with nicely decorated rooms, wooden floor, enough space to feel good. Nice and good modest staff to help and fulfil your wishes - ask for the picnic basket and go to signal hill, it is really worth a try!</p>
  <span class="name">Teo and Family</span>
</div>
<div class="review" style="left:630px">
  <svg class="stars" width="84" height="18" viewBox="0 0 84 18"><g fill="#1e8be6"><polygon points="9,0 11.6,6 18,6.6 13.2,10.8 14.6,17 9,13.7 3.4,17 4.8,10.8 0,6.6 6.4,6"/><polygon transform="translate(21 0)" points="9,0 11.6,6 18,6.6 13.2,10.8 14.6,17 9,13.7 3.4,17 4.8,10.8 0,6.6 6.4,6"/><polygon transform="translate(42 0)" points="9,0 11.6,6 18,6.6 13.2,10.8 14.6,17 9,13.7 3.4,17 4.8,10.8 0,6.6 6.4,6"/></g><polygon transform="translate(63 0)" points="9,0 11.6,6 18,6.6 13.2,10.8 14.6,17 9,13.7 3.4,17 4.8,10.8 0,6.6 6.4,6" fill="#b9cfe6"/></svg>
  <h4>“Worth To Come Again”</h4>
  <div class="avatar" role="img" aria-label="Portrait of a guest in a suit" style="background:linear-gradient(135deg,#d8d8d8,#7d8590)"></div>
  <p>Really good location: in walking distance to almost every spot on the bay. Nice house with nicely decorated rooms, wooden floor, enough space to feel good. Nice and good modest staff to help and fulfil your wishes - ask for the picnic basket and go to signal hill, it is really worth a try!</p>
  <span class="name">Rafe Colby</span>
</div>

<footer class="abs footer">
  <h4 style="left:211px">ABOUT US</h4>
  <p class="col-text" style="left:211px">Lorem ipsum dolor sit amet, consectetur adipiscing elit, sed do eiusmod tempor incididunt ut labore et dolore magna aliqua. Ut enim ad minim veniam, quis nostrud exercitation ullamco laboris nisi ut aliquip ex ea commodo consequat. Duis aute irure dolor in reprehenderit.</p>

  <h4 style="left:410px">CONTACT INFO</h4>
  <div class="contact-row" style="left:410px;top:78px"><svg width="10" height="13" viewBox="0 0 10 13"><path d="M5 0a5 5 0 0 1 5 5c0 3-5 8-5 8S0 8 0 5a5 5 0 0 1 5-5z" fill="#aaa"/><circle cx="5" cy="5" r="1.8" fill="#303233"/></svg><span>1187 Harbor View Rd<br>Grand Cayman</span></div>
  <div class="contact-row" style="left:410px;top:120px"><svg width="10" height="12" viewBox="0 0 10 12"><path d="M2 0h2l1 3-1.5 1.2a7 7 0 0 0 3 3L8 6l2 1v2.5C10 11 9 12 8 12 3.6 12 0 8.4 0 4 0 2 1 0 2 0z" fill="#aaa"/></svg><span>(345) 555-0147<br>(345) 555-0148</span></div>
  <div class="contact-row" style="left:410px;top:160px"><svg width="12" height="9" viewBox="0 0 12 9"><rect width="12" height="9" fill="#aaa"/><polyline points="0,0 6,5 12,0" fill="none" stroke="#303233" stroke-width="1.2"/></svg><span>thedorvallodge@mailnest.example</span></div>
  <div class="footer-social"><span>PalBoard</span><span>Snapgrid</span><span>Chirp</span><span>WorkLink</span></div>

  <h4 style="left:609px">RECENT POSTS</h4>
  <div class="post-row" style="top:76px"><div class="post-thumb" role="img" aria-label="Beach thumbnail"></div><div><b>Sed ut perspiciatis</b><span>21 August, 2015</span></div></div>
  <div class="post-row" style="top:124px"><div class="post-thumb" role="img" aria-label="Pool thumbnail"></div><div><b>Sed ut perspiciatis</b><span>21 August, 2015</span></div></div>
  <div class="post-row" style="top:172px"><div class="post-thumb" role="img" aria-label="Guests thumbnail"></div><div><b>Sed ut perspiciatis</b><span>21 August, 2015</span></div></div>

  <h4 style="left:808px">NEWSLETTER</h4>
  <p class="col-text" style="left:808px">Lorem ipsum dolor sit amet, consectetur adipiscing elit, sed do eiusmod tempor incididunt ut labore et dolore magna aliqua. Ut enim ad minim veniam, quis nostrud exercitation ullamco.</p>
  <div class="email-input">Your Email</div>
  <div class="email-send"><svg width="12" height="9" viewBox="0 0 12 9"><rect width="12" height="9" fill="#fff"/><polyline points="0,0 6,5 12,0" fill="none" stroke="#37b3c7" stroke-width="1.2"/></svg></div>
</footer>

<div class="abs bottom-bar">
  <p>copyright@2015reserved</p>
  <div class="to-top"><svg width="10" height="7"><polyline points="1,6 5,1 9,6" fill="none" stroke="#37b3c7" stroke-width="1.6"/></svg></div>
</div>

</body>
</html>
```